Web Site for Strategy and Technology Consulting Company

We are looking for a website design that engages potential customers to understand our services and contact us. In this contest, we are looking for a homepage design, but the winning designer will be favored for the design of some of the more complicated interior pages of the site. An additional contest (or contests) for these pages will be added soon.

PLATROM AND RESPONSIVE DESIGN
The site will be implemented in WordPress using the Elementor page builder.
We are looking for a design that will look good on phones are well as laptop browsers.

UPLOADED FILES INCLUDE:
1a A wireframe of the homepage we are looking for. The Uploaded PDF also includes a draft of the text proposed for the homepage. Designers are free to go beyond the wireframe, but all elements of the wireframe should be included.
1b A Word document with the draft text of the homepage.
2a-d The Corvanta logo. Two versions are included – a dark version which works well against a light background, and a light version which works well against a dark background.
3 The Corvanta color palette with HEX and RGB values. Designers are not limited to this palette, but colors should be complementary.
4 A draft of the homepage menu
5 Service sheets with information on the services we provide

MORE ABOUT CORVANTA
Corvanta is a consulting company focused on transforming businesses through software. Our tagline, “Transformation Delivered,” recognizes the gap business often have between business transformation and the software they end up with. By listening to our customers and understanding their vision and where they are, we help get our customers where they want to go.

We increase our capability by working with many consultants and partners, allowing us to provide our customers with the best people and the software that best suits them.

Industry/Entity Type

Consulting

Number of Pages Required

1 page

Font styles to use
Sans Serif

Requirements
Must have
• the content represented on the wireframe uploaded
Nice to have
• interactive features, such as roll-over icons that reveal additional information

```html
<!DOCTYPE html>
<html lang="en">
<head>
<meta charset="utf-8">
<title>Corvanta — Transformation Delivered</title>
<link href="https://fonts.googleapis.com/css2?family=Poppins:wght@300;400;500;600;700&display=swap" rel="stylesheet">
<style>
:root{
  --navy:#1b3f73;
  --blue:#1f5fa5;
  --bright:#2a7ccf;
  --sky:#eaf2fb;
  --pale:#f4f8fc;
  --ink:#2e3440;
  --muted:#5b6472;
  --heading:#4a4f58;
  --white:#ffffff;
  --bar:#cddff2;
}
*{box-sizing:border-box;margin:0;padding:0}
html,body{width:1200px;height:4848px;overflow:hidden}
body{font-family:"Poppins",sans-serif;color:var(--ink);background:var(--white);position:relative}
section,header,footer{position:absolute;left:0;width:1200px}
.abs{position:absolute}

/* header */
.site-header{top:0;height:120px;background:var(--white);display:flex;align-items:center;justify-content:space-between;padding:0 80px;z-index:3}
.brand{font-size:44px;font-weight:600;color:var(--navy);letter-spacing:-0.5px}
.nav{display:flex;align-items:center;gap:34px;font-size:16px;color:var(--ink)}
.nav .cta{background:var(--bright);color:var(--white);padding:12px 22px;border-radius:3px}

/* hero */
.hero{top:120px;height:700px;overflow:hidden}
.hero-photo{position:absolute;inset:0;background:linear-gradient(90deg,#f3f4f6 0%,#eceef1 38%,#b9c0c8 62%,#4a5058 85%,#2d3238 100%)}
.hero-kicker{left:128px;top:120px;font-size:26px;color:var(--ink)}
.hero-title{left:128px;top:158px;font-size:48px;font-weight:600;color:var(--bright);line-height:1.1}
.hero-text{left:128px;top:240px;width:380px;font-size:17px;line-height:1.5;color:var(--ink)}
.btn{display:inline-block;background:var(--navy);color:var(--white);font-size:16px;font-weight:500;padding:16px 34px;border-radius:3px}
.hero .btn{position:absolute;left:128px;top:320px}
.hero-cut{position:absolute;left:0;bottom:0}
.scroll-cue{top:815px;left:578px;width:44px;height:44px;border-radius:50%;background:var(--white);border:2px solid var(--navy);z-index:4;display:flex;align-items:center;justify-content:center}

/* story */
.story{top:860px;height:620px}
.photo{border-radius:2px}
.section-title{font-size:58px;font-weight:500;color:var(--heading)}
.body-text{font-size:16px;line-height:1.65;color:var(--muted)}
.ticks{list-style:none}
.ticks li{position:relative;padding-left:34px;margin:12px 0;font-size:16px;line-height:1.5;color:var(--muted)}
.ticks li svg{position:absolute;left:0;top:2px}

/* how we work */
.how{top:1480px;height:1200px;background:var(--sky)}
.center-title{width:100%;text-align:center;font-size:60px;font-weight:500;color:var(--navy)}
.service{left:168px;width:470px;height:132px;border:2px solid #bcd3ee;border-radius:10px;background:var(--pale);display:flex;align-items:center;padding:0 18px;gap:20px}
.service.active{background:var(--white);border-color:var(--blue)}
.service-icon{width:88px;height:88px;border-radius:50%;border:2px dashed var(--blue);flex:none;display:flex;align-items:center;justify-content:center;background:var(--white)}
.service h3{font-size:23px;font-weight:500;color:var(--blue);line-height:1.15;white-space:nowrap}
.service h3.wrap{white-space:normal}
.service p{font-size:16px;color:var(--muted);line-height:1.4;margin-top:4px}

/* team */
.team{top:2680px;height:640px}

/* testimonials */
.testimonials{top:3320px;height:580px;background:var(--blue)}
.testimonials .center-title{color:var(--white)}
.quote-card{top:200px;width:320px;height:260px;border:2px solid #9cc3ec;border-radius:8px;padding:26px 24px;color:var(--white)}
.quote-head{display:flex;gap:18px;align-items:center}
.avatar{width:76px;height:76px;border-radius:50%;background:linear-gradient(135deg,#c9d3de,#7d8a99);border:3px solid var(--white);flex:none}
.quote-head h4{font-size:17px;font-weight:600}
.quote-head span{font-size:13px;opacity:.85;display:block}
.stars{color:#ffc83d;font-size:15px;letter-spacing:2px}
.quote-card p{margin-top:18px;font-size:13px;line-height:1.6}
.arrow-btn{width:40px;height:40px;border-radius:50%;background:var(--white);display:flex;align-items:center;justify-content:center;opacity:.9}

/* technologies */
.tech{top:3900px;height:500px;background:var(--pale)}
.tech-row{top:250px;left:180px;width:840px;display:flex;justify-content:space-around;align-items:center}
.partner{font-size:34px;font-weight:600;color:#3a3f47;display:flex;align-items:center;gap:12px}
.partner i{display:inline-block;width:26px;height:26px;background:#3a3f47}
.tech .arrow-btn{background:#b8c0ca}

/* footer */
.site-footer{top:4340px;height:440px;background:var(--blue);color:var(--white)}
.footer-brand{left:160px;top:200px;font-size:52px;font-weight:600;color:var(--white)}
.socials{left:214px;top:290px;display:flex;gap:10px}
.socials span{width:26px;height:26px;border:2px solid #ffd54a;border-radius:4px}
.footer-col h5{font-size:20px;font-weight:600;margin-bottom:16px;letter-spacing:.5px}
.footer-col li{list-style:none;font-size:16px;margin:8px 0;display:flex;align-items:center;gap:12px}
.dot{width:9px;height:9px;border-radius:50%;background:#ffd54a;flex:none}
.contact-ico{width:26px;height:26px;border:2px solid var(--white);border-radius:4px;flex:none;display:flex;align-items:center;justify-content:center}
.copyright{top:4780px;height:68px;background:var(--bar);color:var(--navy);font-size:14px;display:flex;align-items:center;justify-content:center}
</style>
</head>
<body>

<header class="site-header">
  <div class="brand">Corvanta</div>
  <nav class="nav">
    <span>About Us</span><span>Services</span><span>Insights</span><span>Join Us</span>
    <span class="cta">Contact Us</span>
  </nav>
</header>

<section class="hero">
  <div class="hero-photo" role="img" aria-label="Consultant working on a laptop at a bright office desk"></div>
  <div class="abs hero-kicker">Corvanta</div>
  <h1 class="abs hero-title">Transformation Delivered</h1>
  <p class="abs hero-text">Consulting company focused on transforming businesses through software.</p>
  <span class="btn">READ MORE</span>
  <svg class="hero-cut" width="1200" height="120" viewBox="0 0 1200 120">
    <polygon points="0,50 1200,100 1200,120 0,120" fill="#ffffff"/>
    <polygon points="0,30 1200,80 1200,100 0,50" fill="#1b3f73"/>
  </svg>
</section>
<div class="abs scroll-cue">
  <svg width="14" height="18" viewBox="0 0 14 18"><path d="M7 1v15M2 11l5 5 5-5" fill="none" stroke="#1b3f73" stroke-width="2"/></svg>
</div>

<section class="story">
  <div class="abs photo" style="left:92px;top:40px;width:480px;height:480px;background:linear-gradient(135deg,#e7e9ec,#b7bcc3 55%,#6f6a66)" role="img" aria-label="Consultant at a laptop beside a gavel"></div>
  <h2 class="abs section-title" style="left:600px;top:110px">Our Story</h2>
  <div class="abs" style="left:600px;top:200px;width:500px">
    <p class="body-text">We do more for our customers than implement software. We listen. We work to understand where they are in their transformation journey and where they want to go. We partner with them to clear the roadblocks that stand in their way, ensuring they reach their destination. At Corvanta, we:</p>
    <ul class="ticks" style="margin:16px 0 16px 30px">
      <li><svg width="20" height="20" viewBox="0 0 20 20"><rect x="1" y="1" width="18" height="18" rx="3" fill="none" stroke="#1f5fa5" stroke-width="2"/><path d="M5 10l3.5 3.5L15 6" fill="none" stroke="#1f5fa5" stroke-width="2"/></svg>Focus on business value, with an emphasis on delivering value quickly.</li>
      <li><svg width="20" height="20" viewBox="0 0 20 20"><rect x="1" y="1" width="18" height="18" rx="3" fill="none" stroke="#1f5fa5" stroke-width="2"/><path d="M5 10l3.5 3.5L15 6" fill="none" stroke="#1f5fa5" stroke-width="2"/></svg>Meet our customers where they are without backing them up to the beginning of their journey.</li>
      <li><svg width="20" height="20" viewBox="0 0 20 20"><rect x="1" y="1" width="18" height="18" rx="3" fill="none" stroke="#1f5fa5" stroke-width="2"/><path d="M5 10l3.5 3.5L15 6" fill="none" stroke="#1f5fa5" stroke-width="2"/></svg>Provide a wide range of services, from strategy to product support.</li>
      <li><svg width="20" height="20" viewBox="0 0 20 20"><rect x="1" y="1" width="18" height="18" rx="3" fill="none" stroke="#1f5fa5" stroke-width="2"/><path d="M5 10l3.5 3.5L15 6" fill="none" stroke="#1f5fa5" stroke-width="2"/></svg>Commit to our customer's long-term success.</li>
    </ul>
    <p class="body-text">Corvanta is business transformation, delivered.</p>
  </div>
</section>

<section class="how">
  <h2 class="abs center-title" style="top:100px">How We Work</h2>
  <p class="abs body-text" style="left:168px;top:200px;width:864px;text-align:justify">During our early years, Corvanta focused only on business transformation. We came to realize that successful transformation often depended on quality software implementations, and often more than one. Now we focus on five things, the five things most businesses need to reach their goals.</p>

  <div class="abs service active" style="top:340px"><div class="service-icon"><svg width="36" height="36" viewBox="0 0 36 36"><rect x="7" y="4" width="22" height="28" rx="2" fill="none" stroke="#1f5fa5" stroke-width="2"/><path d="M12 18l4 4 8-8" fill="none" stroke="#1f5fa5" stroke-width="2"/></svg></div><div><h3>Business Transformation</h3><p>Define and execute your strategy.</p></div></div>
  <div class="abs service" style="top:500px"><div class="service-icon"><svg width="36" height="36" viewBox="0 0 36 36"><circle cx="18" cy="18" r="7" fill="none" stroke="#1f5fa5" stroke-width="2"/><circle cx="18" cy="18" r="13" fill="none" stroke="#1f5fa5" stroke-width="2" stroke-dasharray="4 3"/></svg></div><div><h3>ERP Implementations</h3><p>Assess, upgrade, and implement ERP solutions to meet your needs.</p></div></div>
  <div class="abs service" style="top:660px"><div class="service-icon"><svg width="36" height="36" viewBox="0 0 36 36"><circle cx="13" cy="13" r="5" fill="none" stroke="#1f5fa5" stroke-width="2"/><circle cx="24" cy="15" r="4" fill="none" stroke="#1f5fa5" stroke-width="2"/><path d="M4 29c1-6 5-9 9-9s8 3 9 9M20 22c5 0 9 3 10 7" fill="none" stroke="#1f5fa5" stroke-width="2"/></svg></div><div><h3>CRM Implementations</h3><p>Take your relationships to the next level.</p></div></div>
  <div class="abs service" style="top:820px"><div class="service-icon"><svg width="36" height="36" viewBox="0 0 36 36"><path d="M6 30V20M14 30V12M22 30V16M30 30V6" stroke="#1f5fa5" stroke-width="4"/></svg></div><div><h3>BI and Data</h3><p>Discover, connect, and trust your data.</p></div></div>
  <div class="abs service" style="top:980px"><div class="service-icon"><svg width="36" height="36" viewBox="0 0 36 36"><circle cx="18" cy="12" r="6" fill="none" stroke="#1f5fa5" stroke-width="2"/><path d="M6 32c1-8 6-12 12-12s11 4 12 12" fill="none" stroke="#1f5fa5" stroke-width="2"/></svg></div><div><h3 class="wrap">Building the Right Team of People</h3><p>Hire resources for your transformation journey.</p></div></div>

  <div class="abs photo" style="left:672px;top:520px;width:448px;height:420px;background:linear-gradient(135deg,#d9dde2,#a9b1ba 50%,#5e6670)" role="img" aria-label="Collage of colleagues collaborating at laptops"></div>
  <p class="abs body-text" style="top:1142px;width:100%;text-align:center;color:var(--ink)">Find out how Corvanta can help you put all the pieces together and get them done.</p>
</section>

<section class="team">
  <div class="abs" style="left:180px;top:80px;width:260px;height:460px;border:3px dashed var(--blue)"></div>
  <div class="abs photo" style="left:80px;top:170px;width:360px;height:320px;background:linear-gradient(135deg,#c8ccd2,#8c8580 50%,#4b4642)" role="img" aria-label="Consultants meeting around a conference table"></div>
  <h2 class="abs section-title" style="left:600px;top:110px">Our Team</h2>
  <div class="abs" style="left:600px;top:200px;width:500px">
    <p class="body-text">The world has changed in the past twenty years the people you need might not all work for one company. Our clients want the best resources available quickly. That's why, in addition to our team of experts, we partner with:</p>
    <ul class="ticks" style="margin:16px 0 16px 30px">
      <li><svg width="20" height="20" viewBox="0 0 20 20"><rect x="1" y="1" width="18" height="18" rx="3" fill="none" stroke="#1f5fa5" stroke-width="2"/><path d="M5 10l3.5 3.5L15 6" fill="none" stroke="#1f5fa5" stroke-width="2"/></svg>A large network of expert consultants who are the best at what they do.</li>
      <li><svg width="20" height="20" viewBox="0 0 20 20"><rect x="1" y="1" width="18" height="18" rx="3" fill="none" stroke="#1f5fa5" stroke-width="2"/><path d="M5 10l3.5 3.5L15 6" fill="none" stroke="#1f5fa5" stroke-width="2"/></svg>Service providers all over the world to provide the resources and value that are right for you available 24 x 7.</li>
    </ul>
    <p class="body-text">People are invariably at the center of our customer's success. Find out how we can add our experts to yours.</p>
  </div>
</section>

<section class="testimonials">
  <h2 class="abs center-title" style="top:90px;font-size:54px">Testimonials</h2>
  <div class="abs arrow-btn" style="left:28px;top:310px"><svg width="12" height="14" viewBox="0 0 12 14"><path d="M9 1L3 7l6 6" fill="none" stroke="#1f5fa5" stroke-width="2"/></svg></div>
  <div class="abs arrow-btn" style="left:1132px;top:310px"><svg width="12" height="14" viewBox="0 0 12 14"><path d="M3 1l6 6-6 6" fill="none" stroke="#1f5fa5" stroke-width="2"/></svg></div>

  <div class="abs quote-card" style="left:88px"><div class="quote-head"><div class="avatar" role="img" aria-label="Client portrait"></div><div><h4>Jonas Smeed</h4><span>Client Partner</span><div class="stars">★★★★★</div></div></div>
    <p>Corvanta listened first, then delivered. Our ERP rollout landed on time and on budget, and our teams finally work from one shared source of truth.</p></div>
  <div class="abs quote-card" style="left:440px"><div class="quote-head"><div class="avatar" role="img" aria-label="Client portrait"></div><div><h4>Carl Denton</h4><span>Client Partner</span><div class="stars">★★★★★</div></div></div>
    <p>Their consultants understood our goals from day one. The new CRM has reshaped how our sales team works with customers every single week now.</p></div>
  <div class="abs quote-card" style="left:792px"><div class="quote-head"><div class="avatar" role="img" aria-label="Client portrait"></div><div><h4>Stefan Kerr</h4><span>Client Partner</span><div class="stars">★★★★★</div></div></div>
    <p>Corvanta found the right people fast. Their partner network filled every gap in our team, and the results showed within the first quarter.</p></div>
</section>

<section class="tech">
  <h2 class="abs center-title" style="top:80px;font-size:54px">Technologies</h2>
  <div class="abs arrow-btn" style="left:92px;top:262px"><svg width="12" height="14" viewBox="0 0 12 14"><path d="M9 1L3 7l6 6" fill="none" stroke="#fff" stroke-width="2"/></svg></div>
  <div class="abs arrow-btn" style="left:1068px;top:262px"><svg width="12" height="14" viewBox="0 0 12 14"><path d="M3 1l6 6-6 6" fill="none" stroke="#fff" stroke-width="2"/></svg></div>
  <div class="abs tech-row">
    <span class="partner">Nexora</span>
    <span class="partner"><i></i>Quadrel</span>
    <span class="partner">Helix</span>
    <span class="partner">Orbis</span>
  </div>
</section>

<footer class="site-footer">
  <svg class="abs" style="left:0;top:0" width="1200" height="80" viewBox="0 0 1200 80"><path d="M0 0H1200V0C900 80 300 80 0 20Z" fill="#f4f8fc"/></svg>
  <div class="abs footer-brand">Corvanta</div>
  <div class="abs socials"><span></span><span></span><span></span><span></span></div>
  <div class="abs footer-col" style="left:560px;top:170px">
    <h5>QUICK LINKS</h5>
    <ul><li><i class="dot"></i>About Us</li><li><i class="dot"></i>Services</li><li><i class="dot"></i>Insights</li><li><i class="dot"></i>Join Us</li><li><i class="dot"></i>Contact Us</li></ul>
  </div>
  <div class="abs footer-col" style="left:800px;top:170px">
    <h5>CONTACT US</h5>
    <ul>
      <li><span class="contact-ico"><svg width="12" height="12" viewBox="0 0 12 12"><path d="M2 1h3l1 3-2 1a7 7 0 0 0 3 3l1-2 3 1v3c-6 0-10-4-10-10z" fill="#fff"/></svg></span>+012 555 0147</li>
      <li><span class="contact-ico"><svg width="14" height="10" viewBox="0 0 14 10"><rect x="1" y="1" width="12" height="8" fill="none" stroke="#fff" stroke-width="1.5"/><path d="M1 1l6 5 6-5" fill="none" stroke="#fff" stroke-width="1.5"/></svg></span>info@corvanta.com</li>
      <li><span class="contact-ico"><svg width="10" height="14" viewBox="0 0 10 14"><path d="M5 13S1 8 1 5a4 4 0 0 1 8 0c0 3-4 8-4 8z" fill="#fff"/></svg></span><span>Address line Dummy Here<br>Address line Here</span></li>
    </ul>
  </div>
</footer>
<div class="abs copyright" style="width:1200px;left:0">Copyright © 2020 All Rights Reserved by Corvanta</div>

</body>
</html>
```